We have 'joined together' 6 micro-sites with a common theme. Looking to upgrade the design of a total of 26 pages on the abovementioned sites, whilst maintaining a common look and feel.

Goal is to improve customer experience and conversion rate, whilst maintaining Vantro rankings. New design to be responsive to different devices and SEO optimised

We prefer simple designs with the cleaness of Zelqo.com, however with more descriptive text. Target audience are business managers and owners, so site should convey professional capability, with a hint of playfulness. After all data can be fun? No?

See attached doc for further details.

Update: 19/8/2014. Following further consideration, the HTML coding no longer required. Once design is finalised, we require a PSD file for each page showing the full page layout, including all images and icons. We will extract the relevant bits from the PSD and do the coding and css inhouse.
Updates

Hi All The Pelquin Collective - PSD Design Only. HTML no longer required Following further consideration, the HTML / Css coding aspect of the project NO longer required. Once design is finalised, we require a PSD file from you for each of the 26 web pages, showing the page layout and including all images and icons. If one page layout is the same as another, then we request that you just supply images and icons for that page in a PSD file. We will then extract the relevant bits from the PSD and we will do the coding and css inhouse. Our main aim is to get an awesome, blow-your-sox-off design that compels users to convert. Many thanks in anticipation Oliver.

Project Deadline Extended
Reason: Changed deliverables from PSD, HTML and Coding t o PSD only. Hopefully this change will allow previous designers who were not interested to reconsider. Many thanks Oliver

Target Market(s)

Target market is business & IT managers within Australian organisations who are having problems with their data. Site must convey the impression that we are:
1) Very capable
2) Professional in our dealings
3) Reliable & trustworthy
4) Just a little bit quirky

Aprox. 60% of users are female, 40% male. Typically in the 30 to 55 year old bracket.

Number 1 requirements is that we don't embarrass our clients in any way.
2nd is that we do a good high quality job, delivering a good result.

We are not the cheapest nor the most expensive data shop around. We offer good value-for-money solutions. We are also reliable, friendly and available

Industry/Entity Type

Business

Font styles to use
Sans Serif

Requirements
Must have
• Simple yet information dense design. The "who we are" and "what we do" to be immediately visible above the fold. Images to be high quality. Good usability.
Simple navigation structure. Easy for users to find the info that they want.

In summary a simple, but good looking site, that compels users to contact us
Should not have
• No flash, fancy automation, rotating images, pop-ups etc.

```html
<!DOCTYPE html>
<html lang="en">
<head>
<meta charset="utf-8">
<title>The Pelquin Collective — Data Services</title>
<link href="https://fonts.googleapis.com/css2?family=Oswald:wght@300;400;500&family=PT+Sans+Narrow:wght@400;700&display=swap" rel="stylesheet">
<style>
  :root {
    --orange: #e8461c;
    --ink: #2a2a2a;
    --text: #222;
    --footer: #2f2f2f;
    --footer-bar: #1f1f1f;
    --tag: #262626;
    --white: #fff;
    --rule: #c9c9c9;
  }
  * { box-sizing: border-box; margin: 0; padding: 0; }
  html, body { width: 1200px; height: 2500px; overflow: hidden; background: var(--white); }
  body { font-family: "PT Sans Narrow", "Arial Narrow", sans-serif; color: var(--text); position: relative; }

  /* Header */
  .site-header { position: absolute; top: 0; left: 0; width: 1200px; height: 86px; background: var(--white); }
  .brand { position: absolute; left: 38px; top: 14px; font-family: "Oswald", sans-serif; font-weight: 500; font-size: 42px; line-height: 56px; color: var(--ink); }
  .main-nav { position: absolute; right: 40px; top: 0; height: 86px; display: flex; gap: 24px; }
  .main-nav a { font-family: "Oswald", sans-serif; font-size: 16px; color: var(--ink); text-decoration: none; line-height: 100px; height: 86px; position: relative; }
  .main-nav a.active { color: var(--orange); }
  .main-nav a.active::before { content: ""; position: absolute; left: -4px; right: -4px; top: 0; height: 4px; background: var(--orange); }
  .main-nav a.active::after { content: ""; position: absolute; left: -6px; right: -6px; bottom: 0; height: 4px; background: var(--orange); }

  /* Hero */
  .hero { position: absolute; top: 86px; left: 0; width: 1200px; height: 500px;
    background: linear-gradient(160deg, #4a4a4a 0%, #2e2e2e 45%, #1d1d1d 100%);
    clip-path: polygon(0 0, 100% 0, 100% calc(100% - 28px), calc(100% - 44px) 100%, 44px 100%, 0 calc(100% - 28px));
    text-align: center; color: var(--white); }
  .hero-tagline { position: absolute; top: 160px; width: 100%; font-family: "Oswald", sans-serif; font-size: 25px; font-weight: 400; }
  .hero-title { position: absolute; top: 186px; width: 100%; font-family: "Oswald", sans-serif; font-weight: 400; font-size: 112px; line-height: 140px; letter-spacing: 1px; }
  .hero-title span { color: var(--orange); }
  .btn { display: inline-block; background: var(--orange); color: var(--white); font-family: "Oswald", sans-serif; text-decoration: none; text-transform: uppercase; }
  .hero .btn { position: absolute; top: 368px; left: 518px; width: 164px; height: 52px; line-height: 52px; font-size: 16px; }

  /* Section titles */
  .section-title { font-family: "Oswald", sans-serif; font-weight: 400; color: var(--orange); font-size: 44px; line-height: 60px; text-align: center; }
  .divider { position: relative; width: 190px; height: 12px; margin: 6px auto 0; }
  .divider::before { content: ""; position: absolute; left: 0; right: 0; top: 6px; height: 1px; background: var(--rule); }
  .divider::after { content: ""; position: absolute; left: 89px; top: 1px; width: 11px; height: 11px; border-radius: 50%; background: var(--orange); }

  .body-copy { font-size: 17px; line-height: 19px; }

  /* Services */
  .services { position: absolute; top: 606px; left: 0; width: 1200px; text-align: center; }
  .services p { width: 1030px; margin: 24px auto 0; }
  .services p + p { margin-top: 20px; }

  /* Projects */
  .projects { position: absolute; top: 842px; left: 0; width: 1200px; height: 494px;
    background: linear-gradient(180deg, #2b2d30 0%, #222427 100%);
    clip-path: polygon(44px 0, calc(100% - 44px) 0, 100% 28px, 100% calc(100% - 28px), calc(100% - 44px) 100%, 44px 100%, 0 calc(100% - 28px), 0 28px);
    color: var(--white); }
  .projects .section-title { margin-top: 46px; }
  .project-list { position: absolute; top: 155px; left: 0; width: 1200px; display: flex; justify-content: space-between; padding: 0 18px; }
  .project { width: 190px; text-align: center; }
  .project-icon { width: 120px; height: 120px; margin: 0 auto; border-radius: 50%;
    background: radial-gradient(circle at 50% 45%, #f4f4f4 0%, #e6e6e6 55%, #cfcfcf 100%); position: relative; }
  .project-icon::after { content: ""; position: absolute; left: 36px; top: 36px; width: 48px; height: 48px; border-radius: 8px; background: radial-gradient(circle, #e8662f 0%, #5aa7c9 100%); opacity: .55; }
  .project h3 { font-family: "Oswald", sans-serif; font-weight: 400; color: var(--orange); font-size: 21px; line-height: 30px; margin-top: 26px; }
  .project p { font-size: 13px; line-height: 15px; font-weight: 700; margin: 20px auto 0; width: 140px; }
  .project .btn { margin-top: 22px; width: 128px; height: 28px; line-height: 28px; font-size: 12px; text-transform: none; }

  /* Benefits */
  .benefits { position: absolute; top: 1365px; left: 0; width: 1200px; text-align: center; }
  .benefits p { width: 1040px; margin: 22px auto 0; }
  .benefits p.intro { width: 1100px; margin-top: 20px; }
  .benefits strong { font-weight: 700; }

  /* Call to action */
  .cta { position: absolute; top: 1720px; left: 0; width: 1200px; height: 450px;
    background: linear-gradient(180deg, #3a3a3a 0%, #2c2c2c 60%, #333 100%);
    clip-path: polygon(44px 0, calc(100% - 44px) 0, 100% 28px, 100% 100%, 0 100%, 0 28px);
    text-align: center; color: var(--white); }
  .cta h2 { font-family: "Oswald", sans-serif; font-weight: 400; font-size: 78px; line-height: 96px; margin-top: 63px; }
  .cta .sub { font-size: 26px; line-height: 30px; margin-top: 6px; }
  .cta .cta-brand { font-family: "Oswald", sans-serif; font-weight: 500; font-size: 62px; line-height: 80px; margin-top: 30px; }
  .cta .btn-outline { display: inline-block; margin-top: 24px; width: 308px; height: 68px; line-height: 64px; border: 2px solid var(--white); border-radius: 34px; color: var(--orange); font-family: "Oswald", sans-serif; font-size: 26px; text-decoration: none; }

  /* Footer */
  .site-footer { position: absolute; top: 2170px; left: 0; width: 1200px; height: 291px; background: var(--footer); color: var(--white); }
  .footer-col { position: absolute; top: 26px; }
  .footer-brand { font-family: "Oswald", sans-serif; font-weight: 500; font-size: 29px; line-height: 46px; white-space: nowrap; }
  .footer-col h4 { font-family: "Oswald", sans-serif; font-weight: 400; font-size: 22px; line-height: 30px; text-transform: uppercase; }
  .about-brand p { font-size: 15px; line-height: 17px; font-weight: 700; width: 260px; margin-top: 10px; }
  .tags { display: flex; flex-wrap: wrap; gap: 6px 6px; width: 250px; margin-top: 16px; }
  .tags span { background: var(--tag); font-size: 13px; padding: 0 12px; height: 32px; line-height: 32px; }
  .about p { font-size: 13px; line-height: 15px; font-weight: 700; width: 250px; margin-top: 14px; }
  .contact-list { list-style: none; margin-top: 14px; }
  .contact-list li { font-family: "Oswald", sans-serif; font-size: 16px; letter-spacing: 1px; display: flex; align-items: center; gap: 12px; height: 28px; }
  .contact-list svg { width: 14px; height: 14px; fill: var(--orange); }
  .post { display: flex; gap: 10px; margin-top: 10px; }
  .post:first-of-type { margin-top: 12px; }
  .post-thumb { width: 86px; height: 60px; flex: none; background: linear-gradient(135deg, #f2f4f6 0%, #cfdbe6 100%); }
  .post p { font-size: 13px; line-height: 15px; font-weight: 700; width: 160px; }

  .footer-bar { position: absolute; top: 2461px; left: 0; width: 1200px; height: 39px; background: var(--footer-bar); color: var(--white); font-size: 15px; font-weight: 700; }
  .footer-bar .copy { position: absolute; left: 58px; line-height: 39px; }
  .footer-bar .copy a { color: var(--orange); text-decoration: none; }
  .footer-bar .social { position: absolute; right: 50px; top: 0; height: 39px; display: flex; align-items: center; gap: 8px; }
  .social .dot { width: 24px; height: 24px; border-radius: 50%; background: #5d6a78; }
  .social .label { margin-right: 10px; }
</style>
</head>
<body>

<header class="site-header">
  <div class="brand">The Pelquin Collective</div>
  <nav class="main-nav">
    <a class="active" href="#">Home</a>
    <a href="#">Data Analysis</a>
    <a href="#">Data Cleansing</a>
    <a href="#">Data Mining</a>
    <a href="#">Data Scraping</a>
    <a href="#">Data Warehouse</a>
    <a href="#">Blog</a>
    <a href="#">Contact</a>
  </nav>
</header>

<section class="hero" role="img" aria-label="Dark photograph of a desk with a keyboard, mug and a hand on a mouse">
  <p class="hero-tagline">Helping you Creatively Generate Real value from your Data</p>
  <h1 class="hero-title">IT IS <span>CREATIVE</span></h1>
  <a class="btn" href="#">Get Started</a>
</section>

<section class="services">
  <h2 class="section-title">Data Services</h2>
  <div class="divider"></div>
  <p class="body-copy">The Pelquin Collective is a Melbourne based business offering a comprehensive range of data services. We specialise in data analysis, data cleansing, data mining, data scraping and data warehouses.</p>
  <p class="body-copy">Our goal is to help you extract value from your data in the form of pragmatic insights, trends and relationships. And then to analyse, interpret and use these findings in innovative ways that empower you to manage your organisation for greater profit, with improved decision-making and enhanced strategic, tactical and operational insight.</p>
</section>

<section class="projects">
  <h2 class="section-title">Data Project</h2>
  <div class="divider"></div>
  <div class="project-list">
    <div class="project">
      <div class="project-icon" role="img" aria-label="Illustrated chart icon"></div>
      <h3>Data Analysis</h3>
      <p>Lorem Ipsum is simply dummy text of the printing and typesetting industry.</p>
      <a class="btn" href="#">View More</a>
    </div>
    <div class="project">
      <div class="project-icon" role="img" aria-label="Illustrated broom icon"></div>
      <h3>Data Cleansing</h3>
      <p>Lorem Ipsum is simply dummy text of the printing and typesetting industry.</p>
      <a class="btn" href="#">View More</a>
    </div>
    <div class="project">
      <div class="project-icon" role="img" aria-label="Illustrated magnifying glass icon"></div>
      <h3>Data Mining</h3>
      <p>Lorem Ipsum is simply dummy text of the printing and typesetting industry.</p>
      <a class="btn" href="#">View More</a>
    </div>
    <div class="project">
      <div class="project-icon" role="img" aria-label="Illustrated monitor icon"></div>
      <h3>Data Scraping</h3>
      <p>Lorem Ipsum is simply dummy text of the printing and typesetting industry.</p>
      <a class="btn" href="#">View More</a>
    </div>
    <div class="project">
      <div class="project-icon" role="img" aria-label="Illustrated network diagram icon"></div>
      <h3>Data Warehouse</h3>
      <p>Lorem Ipsum is simply dummy text of the printing and typesetting industry.</p>
      <a class="btn" href="#">View More</a>
    </div>
    <div class="project">
      <div class="project-icon" role="img" aria-label="Illustrated broadcast person icon"></div>
      <h3>Data Resources</h3>
      <p>Lorem Ipsum is simply dummy text of the printing and typesetting industry.</p>
      <a class="btn" href="#">View More</a>
    </div>
  </div>
</section>

<section class="benefits">
  <h2 class="section-title">Your Benefits</h2>
  <div class="divider"></div>
  <p class="body-copy intro">Our core speciality is solving business problems that require complex data analysis, cleansing, mining or modelling techniques. Your benefits include:</p>
  <p class="body-copy"><strong>Fast ROI:</strong> Quick access to skilled data professionals, without the overhead of building and maintaining your own infrastructure and team. Our fees are typically small in contrast to the additional profits or savings that our projects generate for our clients.</p>
  <p class="body-copy"><strong>Innovative practical solutions:</strong> We find smart ways to extract useful information from incomplete and disorganised data. We also have extensive industry experience AND the quantitative rigour to generate innovative yet pragmatic value-adding solutions.</p>
  <p class="body-copy"><strong>Connected to major universities.</strong> We have relationships with leading practitioners at major universities and business schools within Australia. This provides us with ready access to extensive expertise and the latest developments. We have never turned down a project due to it being too complex.</p>
  <p class="body-copy"><strong>Always confidential</strong> and discreet.</p>
</section>

<section class="cta" role="img" aria-label="Dimmed photograph of a workspace with a monitor">
  <h2>GET IN TOUCH WITH US</h2>
  <p class="sub">Lorem Ipsum is simply dummy text of the printing and typesetting industry.</p>
  <p class="cta-brand">The Pelquin Collective</p>
  <a class="btn-outline" href="#">CONTACT US NOW</a>
</section>

<footer class="site-footer">
  <div class="footer-col about-brand" style="left:40px;">
    <div class="footer-brand">The Pelquin Collective</div>
    <p>Lorem Ipsum is simply dummy text of the printing and typesetting industry. Lorem Ipsum has been the industry's standard dummy text ever since the 1500s, Lorem Ipsum is simply dummy text of the printing and typesetting industry. Lorem Ipsum has been the industry's standard dummy text ever since the 1500s,</p>
  </div>
  <div class="footer-col" style="left:332px;">
    <h4>Categories</h4>
    <div class="tags">
      <span>Blogroll</span><span>Featured</span><span>News</span>
      <span>Photographers</span><span>Photography</span>
      <span>Sculptures</span><span>Featured</span><span>News</span>
      <span>Photographers</span><span>Photography</span>
      <span>Sculptures</span><span>Featured</span><span>News</span>
    </div>
  </div>
  <div class="footer-col about" style="left:620px;">
    <h4>About Us</h4>
    <p>Lorem Ipsum is simply dummy text of the printing and typesetting industry.Lorem Ipsum is simply dummy text of the printing and typesetting industry.Lorem Ipsum is simply dummy text of the printing and typesetting industry.</p>
    <ul class="contact-list">
      <li><svg viewBox="0 0 16 16"><path d="M3.6 1l2.4 3-1.4 1.6c.9 2 2.6 3.7 4.6 4.6L10.8 8.8l3 2.4-1.2 2.9C7 14 2 9 1.9 3.4z"/></svg>12 345 6789</li>
      <li><svg viewBox="0 0 16 16"><path d="M1 3h14v1.5L8 9 1 4.5z M1 6.2l7 4.5 7-4.5V13H1z"/></svg>INFO@YOURSITE.COM</li>
      <li><svg viewBox="0 0 16 16"><path d="M8 1.5l7 6.2h-2V14H9.8v-4H6.2v4H3V7.7H1z"/></svg>WWW.YOURSITE.COM</li>
    </ul>
  </div>
  <div class="footer-col" style="left:914px;">
    <h4>Recent Post</h4>
    <div class="post"><div class="post-thumb" role="img" aria-label="Dashboard screenshot thumbnail"></div><p>Lorem Ipsum is simply dummy text of the printing and typesetting industry.</p></div>
    <div class="post"><div class="post-thumb" role="img" aria-label="Dashboard screenshot thumbnail"></div><p>Lorem Ipsum is simply dummy text of the printing and typesetting industry.</p></div>
    <div class="post"><div class="post-thumb" role="img" aria-label="Dashboard screenshot thumbnail"></div><p>Lorem Ipsum is simply dummy text of the printing and typesetting industry.</p></div>
  </div>
</footer>

<div class="footer-bar">
  <p class="copy">copyright by <a href="#">yoursite.com</a> &nbsp;|&nbsp; Privacy Policy</p>
  <div class="social">
    <span class="label">Follow Us</span>
    <span class="dot" role="img" aria-label="Social link"></span>
    <span class="dot" role="img" aria-label="Social link"></span>
    <span class="dot" role="img" aria-label="Social link"></span>
  </div>
</div>

</body>
</html>
```